Aged Care Consultancy Business needs a business card design

I need a two sided business card - I want it clean and professional. Surprise me

Target Market(s)

middle aged and ageing victorians

Industry/Entity Type

Health Care

Contact Information for Business Card

Text to be included

Logo
Aged Care Consulting Services
Professional, Reliable, Affordable

Tovan Brelsick
Director
0427 31 64 92 (larger)
1300 73 29 41
tovan@wadolire.com.au
www.wadolcare.com.au
Facebook (details TBA)

include little icons beside the contact info:

- Envelope = email
- Phone = phone
- Globe = website

Font styles to use
Serif
Sans Serif

Requirements
Must have
• look proffesional and clean

```html
<!DOCTYPE html>
<html lang="en">
<head>
<meta charset="utf-8">
<title>Wadol Care – Business Card</title>
<link rel="stylesheet" href="https://fonts.googleapis.com/css2?family=Nunito:wght@800&family=Open+Sans:wght@400;600&display=swap">
<style>
  :root {
    --blue: #1f4fa0;
    --blue-deep: #173f88;
    --blue-light: #2a5fb6;
    --gold: #eab530;
    --white: #ffffff;
    --paper: #fbfbfb;
    --stage: #e9ebef;
  }
  * { box-sizing: border-box; margin: 0; padding: 0; }
  html, body { width: 1200px; height: 780px; overflow: hidden; }
  body {
    background: var(--stage);
    font-family: "Open Sans", Arial, sans-serif;
    display: flex;
    align-items: center;
    justify-content: center;
    gap: 50px;
  }
  .card {
    position: relative;
    width: 540px;
    height: 310px;
    border-radius: 16px;
    overflow: hidden;
    box-shadow: 0 6px 18px rgba(20, 40, 80, .18);
  }

  /* Front */
  .card--front { background: var(--paper); }
  .card__wave { position: absolute; inset: 0; width: 100%; height: 100%; }
  .front__brand {
    position: absolute;
    left: 44px;
    top: 180px;
    font-family: "Nunito", Arial, sans-serif;
    font-weight: 800;
    font-size: 40px;
    color: var(--blue);
    letter-spacing: .5px;
  }
  .front__divider {
    position: absolute;
    left: 228px;
    top: 36px;
    width: 1px;
    height: 120px;
    background: var(--gold);
  }
  .front__details { position: absolute; left: 250px; top: 32px; }
  .person__name {
    font-size: 16px;
    font-weight: 600;
    color: var(--blue);
    text-transform: uppercase;
    letter-spacing: .3px;
    line-height: 1.1;
  }
  .person__role { font-size: 12px; color: var(--gold); margin-bottom: 12px; }
  .contact-list { list-style: none; }
  .contact-list__item {
    display: flex;
    align-items: center;
    gap: 7px;
    font-size: 12px;
    color: var(--blue);
    line-height: 1;
    margin-bottom: 5px;
  }
  .contact-list__item--main { font-size: 15px; }
  .contact-icon {
    width: 14px;
    height: 14px;
    flex: none;
    border-radius: 3px;
    background: var(--gold);
    display: flex;
    align-items: center;
    justify-content: center;
  }
  .contact-icon svg { width: 10px; height: 10px; }

  /* Back */
  .card--back {
    background: radial-gradient(circle at 55% 40%, var(--blue-light), var(--blue-deep) 80%);
    color: var(--white);
  }
  .back__brand {
    position: absolute;
    left: 0;
    right: 0;
    top: 92px;
    text-align: center;
    font-family: "Nunito", Arial, sans-serif;
    font-weight: 800;
    font-size: 56px;
    color: var(--white);
  }
  .back__tagline {
    position: absolute;
    left: 0;
    right: 0;
    top: 180px;
    text-align: center;
    font-size: 14px;
    line-height: 1.5;
  }
</style>
</head>
<body>

<section class="card card--front" aria-label="Card front">
  <svg class="card__wave" viewBox="0 0 540 310" preserveAspectRatio="none" aria-hidden="true">
    <path d="M120 310 C 330 300 470 190 540 6" fill="none" stroke="var(--gold)" stroke-width="5"/>
    <path d="M170 310 C 350 300 480 200 540 40 L540 310 Z" fill="var(--blue)"/>
  </svg>

  <div class="front__brand">wadol care</div>
  <div class="front__divider"></div>

  <div class="front__details">
    <p class="person__name">Tovan Brelsick</p>
    <p class="person__role">Director</p>
    <ul class="contact-list">
      <li class="contact-list__item contact-list__item--main">
        <span class="contact-icon"><svg viewBox="0 0 10 10"><path d="M2 1h2l1 2-1.2.8a5 5 0 0 0 2.4 2.4L7 5l2 1v2c0 .6-.4 1-1 1A8 8 0 0 1 1 2c0-.6.4-1 1-1z" fill="var(--white)"/></svg></span>
        0427 31 64 92
      </li>
      <li class="contact-list__item">
        <span class="contact-icon"><svg viewBox="0 0 10 10"><path d="M2 1h2l1 2-1.2.8a5 5 0 0 0 2.4 2.4L7 5l2 1v2c0 .6-.4 1-1 1A8 8 0 0 1 1 2c0-.6.4-1 1-1z" fill="var(--white)"/></svg></span>
        1300 73 29 41
      </li>
      <li class="contact-list__item">
        <span class="contact-icon"><svg viewBox="0 0 10 10"><rect x="1" y="2.5" width="8" height="5.5" fill="none" stroke="var(--white)" stroke-width="1"/><path d="M1 2.5l4 3 4-3" fill="none" stroke="var(--white)" stroke-width="1"/></svg></span>
        tovan@wadolire.com.au
      </li>
      <li class="contact-list__item">
        <span class="contact-icon"><svg viewBox="0 0 10 10"><circle cx="5" cy="5" r="3.8" fill="none" stroke="var(--white)" stroke-width=".9"/><ellipse cx="5" cy="5" rx="1.6" ry="3.8" fill="none" stroke="var(--white)" stroke-width=".8"/><path d="M1.2 5h7.6" stroke="var(--white)" stroke-width=".8"/></svg></span>
        www.wadolcare.com.au
      </li>
      <li class="contact-list__item">
        <span class="contact-icon"></span>
        www.kinspace.com
      </li>
    </ul>
  </div>
</section>

<section class="card card--back" aria-label="Card back">
  <div class="back__brand">wadol care</div>
  <p class="back__tagline">Aged Care Consulting Services<br>Professional, Reliable, Affordable</p>
</section>

</body>
</html>
```